Letterhead and Corporate Stationary Design Project

I would like the following designed:
1. Corporate Letterhead
2. Compliment Slips
3. Business Cards(2)

I have attached word document that outlines the text to be contained for all 3. The logo is fine as is and can be used in the design.
I only need letterhead to be designed for contest, the successful applicant can desisgn other 2 items after being awarded the job

Target Market(s)

Information Technology

Industry/Entity Type

Business

Requirements
Must have
• Border around entire letter that matches colours in logo
Clearly identifiable letterhead and footer
Nice to have
• Watermark

```html
<!DOCTYPE html>
<html lang="en">
<head>
<meta charset="utf-8">
<title>Corvane Business Solutions – Letterhead</title>
<link href="https://fonts.googleapis.com/css2?family=Arimo:wght@400;600&display=swap" rel="stylesheet">
<style>
  :root {
    --canvas: #ffffff;
    --paper: #ffffff;
    --brand-blue: #1391dd;
    --brand-navy: #1f3a8a;
    --muted-grey: #b9b9b9;
    --wash-blue: #e3f1fb;
    --wash-grey: #f5f5f5;
    --wash-slate: #e4e9f2;
  }
  * { margin: 0; padding: 0; box-sizing: border-box; }
  html, body {
    width: 1200px;
    height: 1000px;
    overflow: hidden;
    background: var(--canvas);
    font-family: "Arimo", Arial, sans-serif;
  }
  .letterhead {
    position: absolute;
    left: 299px;
    top: 70px;
    width: 606px;
    height: 855px;
    background: var(--paper);
    box-shadow: 0 0 40px rgba(0, 0, 0, 0.18);
  }
  .letterhead__art {
    position: absolute;
    inset: 0;
  }
  .brand {
    position: absolute;
    right: 20px;
    top: 24px;
    display: flex;
    align-items: center;
    gap: 12px;
    color: var(--brand-blue);
    font-weight: 600;
  }
  .brand__dot {
    width: 30px;
    height: 30px;
    border-radius: 50%;
    background: var(--brand-navy);
  }
  .brand__name {
    text-align: right;
    line-height: 1;
  }
  .brand__word {
    display: block;
    font-size: 36px;
    letter-spacing: 0.5px;
  }
  .brand__tagline {
    display: block;
    font-size: 12.5px;
    letter-spacing: 1.6px;
    margin-top: 3px;
  }
  .contact {
    position: absolute;
    right: 20px;
    top: 75px;
    text-align: right;
    font-size: 9px;
    line-height: 11px;
    color: var(--muted-grey);
  }
  .company-details {
    position: absolute;
    right: 20px;
    top: 786px;
    text-align: right;
    font-size: 9.5px;
    line-height: 12px;
    color: var(--brand-navy);
  }
</style>
</head>
<body>
  <main class="letterhead">
    <svg class="letterhead__art" width="606" height="855" viewBox="0 0 606 855" aria-hidden="false">
      <defs>
        <clipPath id="page-inner">
          <rect x="10" y="9" width="585" height="837" rx="20" ry="20"/>
        </clipPath>
      </defs>
      <g clip-path="url(#page-inner)" role="img" aria-label="Faint brand watermark shapes across the lower half of the page">
        <circle class="watermark watermark--main" cx="276" cy="500" r="185" fill="var(--wash-blue)"/>
        <circle class="watermark watermark--left" cx="80" cy="682" r="95" fill="var(--wash-grey)"/>
        <circle class="watermark watermark--corner" cx="475" cy="750" r="135" fill="var(--wash-slate)"/>
      </g>
      <rect class="border-frame" x="10" y="9" width="585" height="837" rx="20" ry="20"
            fill="none" stroke="var(--brand-blue)" stroke-width="5"/>
    </svg>

    <header class="brand">
      <span class="brand__dot"></span>
      <span class="brand__name">
        <span class="brand__word">corvane</span>
        <span class="brand__tagline">BUSINESS SOLUTIONS</span>
      </span>
    </header>

    <address class="contact" style="font-style: normal;">
      Corvane Business Solutions, Harbour Court, 8 Mill Street, Kells, Co. Louth, Ireland<br>
      www.corvane.ie<br>
      Telephone:&nbsp; + 353 41 5550184
    </address>

    <footer class="company-details">
      Corvane Business Solutions Limited<br>
      Company Registration 512639<br>
      VAT No IE7319046K
    </footer>
  </main>
</body>
</html>
```